Brevik Fabrication - Business Card Design

We would like a dark (likely black) themed business card to be able to hand out to potential clients. We may list our services on the card or keep it clean. Unsure. Logo attached

```html
<!DOCTYPE html>
<html lang="en">
<head>
<meta charset="utf-8">
<title>Brevik Fabrication – Business Card</title>
<link rel="stylesheet" href="https://fonts.googleapis.com/css2?family=Work+Sans:wght@400;500;800&display=swap">
<style>
  :root {
    --backdrop: #3a3431;
    --card-black: #121212;
    --gloss-grey: #2e2e2e;
    --brand-blue: #3f86e8;
    --brand-orange: #ef4b23;
    --text-white: #ffffff;
  }
  html, body {
    margin: 0;
    padding: 0;
    width: 800px;
    height: 1200px;
    overflow: hidden;
    background: var(--backdrop);
    font-family: "Work Sans", sans-serif;
  }
  .canvas {
    position: relative;
    width: 800px;
    height: 1200px;
  }
  .card {
    position: absolute;
    left: 80px;
    width: 640px;
    height: 366px;
    background: var(--card-black);
    overflow: hidden;
    box-shadow: 0 14px 30px rgba(0,0,0,0.45);
  }
  .card-front { top: 170px; }
  .card-back  { top: 664px; }

  /* front */
  .front-mark {
    position: absolute;
    inset: 0;
    display: flex;
    align-items: center;
    justify-content: center;
    gap: 16px;
  }
  .front-mark .mark-dot {
    width: 40px;
    height: 40px;
    border-radius: 50%;
    background: var(--gloss-grey);
  }
  .front-mark .mark-name {
    font-weight: 800;
    font-size: 40px;
    letter-spacing: 1px;
    text-transform: uppercase;
    color: var(--gloss-grey);
  }

  /* back */
  .waves {
    position: absolute;
    inset: 0;
    width: 640px;
    height: 366px;
  }
  .back-mark {
    position: absolute;
    left: 30px;
    top: 62px;
    display: flex;
    align-items: center;
    gap: 10px;
  }
  .back-mark .mark-dot {
    width: 26px;
    height: 26px;
    border-radius: 50%;
    background: var(--brand-orange);
  }
  .back-mark .mark-name {
    font-weight: 800;
    font-size: 25px;
    text-transform: uppercase;
    color: var(--brand-blue);
  }
  .holder {
    position: absolute;
    right: 30px;
    top: 90px;
    text-align: right;
  }
  .holder-name {
    font-size: 19px;
    font-weight: 400;
    color: var(--brand-blue);
    text-transform: uppercase;
    letter-spacing: 0.5px;
  }
  .holder-role {
    font-size: 14px;
    color: var(--text-white);
    margin-top: 2px;
  }
  .holder-accent {
    position: absolute;
    right: 0;
    top: 100px;
    width: 8px;
    height: 24px;
    background: var(--brand-orange);
  }
  .contact-list {
    position: absolute;
    right: 30px;
    top: 246px;
    margin: 0;
    padding: 0;
    list-style: none;
    text-align: right;
    color: var(--text-white);
    font-size: 14px;
    line-height: 20px;
  }
  .contact-list li {
    display: flex;
    justify-content: flex-end;
    align-items: center;
    gap: 7px;
  }
  .contact-list svg { width: 12px; height: 12px; }
  .contact-list .no-icon { margin-right: 19px; }
</style>
</head>
<body>
<div class="canvas">

  <section class="card card-front" aria-label="Card front">
    <div class="front-mark">
      <span class="mark-dot"></span>
      <span class="mark-name">Brevik Fabrication</span>
    </div>
  </section>

  <section class="card card-back" aria-label="Card back">
    <svg class="waves" viewBox="0 0 640 366" aria-hidden="true">
      <path class="wave-orange" d="M0,124 C130,200 270,230 420,216 C520,206 590,186 640,180 L640,366 L0,366 Z" fill="var(--brand-orange)"/>
      <path d="M0,144 C130,214 270,238 420,224 C520,214 590,194 640,188 L640,366 L0,366 Z" fill="var(--card-black)"/>
      <path class="wave-blue-line" d="M0,152 C130,222 270,246 420,232 C520,222 590,202 640,196 L640,366 L0,366 Z" fill="var(--brand-blue)"/>
      <path d="M0,158 C130,228 270,252 420,238 C520,228 590,208 640,202 L640,366 L0,366 Z" fill="var(--card-black)"/>
      <path class="wave-blue" d="M0,166 C130,236 270,260 420,246 C520,236 590,216 640,210 L640,366 L0,366 Z" fill="var(--brand-blue)"/>
    </svg>

    <div class="back-mark">
      <span class="mark-dot"></span>
      <span class="mark-name">Brevik Fabrication</span>
    </div>

    <div class="holder">
      <div class="holder-name">Daniel Orsen</div>
      <div class="holder-role">Founder</div>
    </div>
    <span class="holder-accent"></span>

    <ul class="contact-list">
      <li>(555) 214-7730
        <svg viewBox="0 0 12 12" aria-hidden="true"><path d="M2,1 L4.5,1 L5.5,3.5 L4,4.6 C4.6,6 6,7.4 7.4,8 L8.5,6.5 L11,7.5 L11,10 C6,10.5 1.5,6 2,1 Z" fill="#fff"/></svg>
      </li>
      <li>info@brevikfab.com
        <svg viewBox="0 0 12 12" aria-hidden="true"><rect x="1" y="2.5" width="10" height="7" fill="none" stroke="#fff" stroke-width="1.2"/><path d="M1,2.5 L6,6.5 L11,2.5" fill="none" stroke="#fff" stroke-width="1.2"/></svg>
      </li>
      <li>www.brevikfab.com
        <svg viewBox="0 0 12 12" aria-hidden="true"><circle cx="6" cy="6" r="5" fill="none" stroke="#fff" stroke-width="1.1"/><ellipse cx="6" cy="6" rx="2.2" ry="5" fill="none" stroke="#fff" stroke-width="1"/><path d="M1,6 L11,6" stroke="#fff" stroke-width="1"/></svg>
      </li>
      <li><span class="no-icon">218 Harlow Street</span></li>
      <li><span class="no-icon">Fairmont, WI 53090</span></li>
    </ul>
  </section>

</div>
</body>
</html>
```